New cool to-go cup for Kettlewick Coffee

We are looking for a new cool design for our to-go cups in kraft paper (same style as the attached photo).

The idea:

We have three different cups sizes: 6oz, 8oz and 12oz. We call them “One-Sixty” (6oz), “Two-Forty” (8oz) and “Three-sixty” (12oz) (refers to the size in milliliters). We would like to include this in the cup design. Please see the attached sketch of the idea ("Design ideas - Front").

The backside of the cup should have the attached text and logo ("Design ideas - Back").

But other ideas are also very welcome too! Maybe just a simple cup with the logo.

Please keep the design very minimalistic. The more simple the better.

Target Market(s)

Young urban people

Industry/Entity Type

Coffee shop

Font styles to use
Sans Serif

Requirements
Must have
• Kraft paper cups

```html
<!DOCTYPE html>
<html lang="en">
<head>
<meta charset="utf-8">
<title>Kettlewick Coffee – to-go cup wraps</title>
<link rel="stylesheet" href="https://fonts.googleapis.com/css2?family=Open+Sans:wght@400;700&family=Montserrat:wght@700&display=swap">
<style>
  :root {
    --page: #f7f5f2;
    --kraft: #d8bea7;
    --kraft-edge: #c9ad95;
    --ink: #3a2218;
  }
  * { box-sizing: border-box; margin: 0; padding: 0; }
  html, body { width: 1200px; height: 1200px; overflow: hidden; }
  body {
    background: var(--page);
    font-family: "Open Sans", Arial, sans-serif;
    color: var(--ink);
    display: flex;
    flex-direction: column;
    align-items: center;
    justify-content: center;
    gap: 34px;
  }
  .cup-wrap { position: relative; }
  .cup-wrap--160 { width: 860px; height: 300px; }
  .cup-wrap--240 { width: 960px; height: 340px; }
  .cup-wrap--360 { width: 1060px; height: 380px; }
  .wrap-shape { position: absolute; inset: 0; width: 100%; height: 100%; }
  .wrap-shape .paper { fill: var(--kraft); stroke: var(--kraft-edge); stroke-width: 2; }
  .wrap-shape .die-line { fill: none; stroke: var(--ink); stroke-width: 1; }
  .wrap-front, .wrap-back {
    position: absolute; top: 0; bottom: 0; width: 50%;
    display: flex; flex-direction: column; align-items: center; justify-content: center;
    text-align: center;
  }
  .wrap-front { left: 0; }
  .wrap-back { right: 0; }
  .size-tag { font-size: 40px; font-weight: 400; letter-spacing: 0.2px; }
  .size-tag strong { font-weight: 700; }
  .cup-wrap--160 .size-tag { font-size: 34px; }
  .cup-wrap--360 .size-tag { font-size: 46px; }
  .brand {
    display: flex; align-items: center; gap: 8px;
    font-weight: 700; font-size: 21px; letter-spacing: 0.5px;
    margin-bottom: 14px;
  }
  .brand-dot { width: 14px; height: 14px; border-radius: 50%; background: var(--ink); }
  .back-note { font-size: 13.5px; line-height: 1.2; }
  .back-url {
    font-family: "Montserrat", Arial, sans-serif;
    font-weight: 700; font-size: 18px; margin-top: 8px;
  }
  .back-handle { font-size: 12px; margin-top: 8px; }
</style>
</head>
<body>

<section class="cup-wrap cup-wrap--160" aria-label="6oz cup wrap">
  <svg class="wrap-shape" viewBox="0 0 1000 300" preserveAspectRatio="none">
    <path class="paper" d="M10 28 Q500 -6 990 28 L930 292 Q500 270 70 292 Z"/>
    <path class="die-line" d="M24 38 Q500 6 976 38 L920 282 Q500 260 80 282 Z" vector-effect="non-scaling-stroke"/>
  </svg>
  <div class="wrap-front"><p class="size-tag"><strong>#one</strong>sixty</p></div>
  <div class="wrap-back">
    <p class="brand"><span class="brand-dot"></span>Kettlewick Coffee</p>
    <p class="back-note">Read about your coffee<br>and the dedicated farmers<br>who made this cup possible:</p>
    <p class="back-url">www.kettlewick.example</p>
    <p class="back-handle">@kettlewickcups</p>
  </div>
</section>

<section class="cup-wrap cup-wrap--240" aria-label="8oz cup wrap">
  <svg class="wrap-shape" viewBox="0 0 1000 340" preserveAspectRatio="none">
    <path class="paper" d="M10 30 Q500 -6 990 30 L930 332 Q500 308 70 332 Z"/>
    <path class="die-line" d="M24 40 Q500 6 976 40 L920 322 Q500 298 80 322 Z" vector-effect="non-scaling-stroke"/>
  </svg>
  <div class="wrap-front"><p class="size-tag"><strong>#two</strong>forty</p></div>
  <div class="wrap-back">
    <p class="brand"><span class="brand-dot"></span>Kettlewick Coffee</p>
    <p class="back-note">Read about your coffee<br>and the dedicated farmers<br>who made this cup possible:</p>
    <p class="back-url">www.kettlewick.example</p>
    <p class="back-handle">@kettlewickcups</p>
  </div>
</section>

<section class="cup-wrap cup-wrap--360" aria-label="12oz cup wrap">
  <svg class="wrap-shape" viewBox="0 0 1000 380" preserveAspectRatio="none">
    <path class="paper" d="M10 32 Q500 -6 990 32 L930 372 Q500 346 70 372 Z"/>
    <path class="die-line" d="M24 42 Q500 6 976 42 L920 362 Q500 336 80 362 Z" vector-effect="non-scaling-stroke"/>
  </svg>
  <div class="wrap-front"><p class="size-tag"><strong>#three</strong>sixty</p></div>
  <div class="wrap-back">
    <p class="brand"><span class="brand-dot"></span>Kettlewick Coffee</p>
    <p class="back-note">Read about your coffee<br>and the dedicated farmers<br>who made this cup possible:</p>
    <p class="back-url">www.kettlewick.example</p>
    <p class="back-handle">@kettlewickcups</p>
  </div>
</section>

</body>
</html>
```